School Learner profile graphic representation

I have a set of ideas around communicating our school 'learner profile'. These represent the attitudes, habits and dispositions we are trying to develop through our curriculum and wider enrichment programme. I want the links between the ideas and concepts to be represented in some form of an inforgraphic which can be published and displayed for the whole community to connect with. we run two schools and want the profile to represent for both.

Target Market(s)

Students, Parents, Teachers, Wider community in education

Industry/Entity Type

Education

Font styles to use
Other font styles liked:
• Johnson p22

Colors

Designer to choose colors to be used in the design.

Requirements
Must have
• See my diagram in the ppt.
• The statements Aspiration, Agency, Agility, Altitude with the supporting descriptions. Ideally the values in the center is also represented. The two school logos should also be present somehow (both emblems at least). Let me know if the full logo files are required
Nice to have
• the numbering shown in my diagram is not absolutely necessary is it is not necessarily a linear process and rather cyclical and cross reinforcing

```html
<!DOCTYPE html>
<html lang="en">
<head>
<meta charset="utf-8">
<title>Envisioning Our Learners – 4 A's</title>
<link href="https://fonts.googleapis.com/css2?family=Montserrat:wght@300;400;500;600;700;800&display=swap" rel="stylesheet">
<style>
  :root {
    --brand-red: #b52a2e;
    --deep-red: #9a3322;
    --bright-red: #e5402c;
    --path-red: #b23a26;
    --value-red: #d4161d;
    --royal-blue: #3639bb;
    --soft-blue: #7b85d8;
    --ink: #111111;
    --text-grey: #444444;
    --mark-grey: #3c3c3c;
    --panel: #f1f1f1;
    --paper: #ffffff;
  }
  * { margin: 0; padding: 0; box-sizing: border-box; }
  html, body { width: 976px; height: 1200px; overflow: hidden; background: var(--paper); }
  body { font-family: "Montserrat", sans-serif; color: var(--text-grey); }

  .profile-sheet { position: relative; width: 976px; height: 1200px; background: var(--panel); overflow: hidden; }

  .masthead { position: absolute; left: 0; top: 0; width: 976px; height: 159px; background: var(--paper); }
  .masthead-rule { position: absolute; left: 0; top: 159px; width: 976px; height: 10px; background: var(--path-red); }
  .footer-band { position: absolute; left: 0; bottom: 0; width: 976px; height: 24px; background: var(--brand-red); }

  .school-dot { position: absolute; border-radius: 50%; background: var(--brand-red); }
  .school-dot--private { left: 57px; top: 25px; width: 114px; height: 114px; }
  .school-dot--community { left: 596px; top: 26px; width: 112px; height: 112px; }

  .school-name--private {
    position: absolute; left: 181px; top: 52px;
    font-weight: 800; font-size: 25px; letter-spacing: -1px; color: var(--ink); white-space: nowrap;
  }
  .school-tagline {
    position: absolute; left: 181px; top: 86px;
    font-weight: 400; font-size: 19px; letter-spacing: 2.6px; color: var(--ink); white-space: nowrap;
  }
  .school-name--community {
    position: absolute; left: 720px; top: 34px;
    font-weight: 700; font-size: 24px; line-height: 32px; letter-spacing: 3px; color: var(--mark-grey);
    text-transform: uppercase;
  }

  .sheet-title {
    position: absolute; left: 0; top: 176px; width: 976px; text-align: center;
    font-weight: 800; font-size: 38px; color: var(--brand-red); letter-spacing: 0.3px;
  }
  .sheet-subtitle {
    position: absolute; left: 0; top: 222px; width: 976px; text-align: center;
    font-weight: 800; font-size: 40px; color: var(--royal-blue);
  }

  .profile-art { position: absolute; left: 0; top: 0; }

  .trait { position: absolute; width: 240px; font-size: 15.5px; line-height: 19.5px; font-weight: 500; color: var(--text-grey); }
  .trait--left { left: 49px; text-align: left; }
  .trait--right { right: 48px; text-align: right; }
  .trait--top { top: 274px; }
  .trait--bottom { top: 693px; }
  .trait-label { font-size: 15.5px; font-weight: 500; margin-bottom: 6px; }
  .trait-label strong { font-size: 21px; font-weight: 600; color: #3a3a3a; }
  .trait--agility { width: 215px; }
  .trait--agency { width: 245px; }

  .value-word { font-family: "Montserrat", sans-serif; font-weight: 600; font-size: 29px; fill: var(--value-red); letter-spacing: 1px; }
</style>
</head>
<body>
<main class="profile-sheet">
  <header class="masthead">
    <span class="school-dot school-dot--private"></span>
    <div class="school-name--private">Crescent Bay Private School</div>
    <div class="school-tagline">Where every child is special</div>
    <span class="school-dot school-dot--community"></span>
    <div class="school-name--community">Crescent Bay<br>Community<br>School</div>
  </header>
  <div class="masthead-rule"></div>

  <h1 class="sheet-title">Envisioning Our Learners</h1>
  <h2 class="sheet-subtitle">4 A’s</h2>

  <svg class="profile-art" width="976" height="1200" viewBox="0 0 976 1200">
    <defs>
      <linearGradient id="red-disc" x1="0" y1="0" x2="1" y2="0">
        <stop offset="0" stop-color="#e5402c"/>
        <stop offset="1" stop-color="#8e3120"/>
      </linearGradient>
      <linearGradient id="red-rim" x1="0" y1="0" x2="1" y2="0">
        <stop offset="0" stop-color="#8e3120"/>
        <stop offset="1" stop-color="#e5402c"/>
      </linearGradient>
      <linearGradient id="blue-disc" x1="0" y1="0" x2="1" y2="0">
        <stop offset="0" stop-color="#7b85d8"/>
        <stop offset="1" stop-color="#2a30b0"/>
      </linearGradient>
      <linearGradient id="blue-rim" x1="0" y1="0" x2="1" y2="0">
        <stop offset="0" stop-color="#2a30b0"/>
        <stop offset="1" stop-color="#7b85d8"/>
      </linearGradient>
      <radialGradient id="compass-fill" cx="0.5" cy="0.5" r="0.5">
        <stop offset="0" stop-color="#eee3e6"/>
        <stop offset="0.75" stop-color="#ddccd0"/>
        <stop offset="1" stop-color="#c9a9b0"/>
      </radialGradient>
      <filter id="disc-shadow" x="-30%" y="-30%" width="170%" height="170%">
        <feDropShadow dx="10" dy="12" stdDeviation="10" flood-color="#000" flood-opacity="0.25"/>
      </filter>
      <path id="value-ring" d="M 608 1010 A 130 130 0 1 1 348 1010 A 130 130 0 1 1 608 1010"/>
    </defs>

    <!-- connecting paths -->
    <g class="links" fill="none" stroke-width="15">
      <path stroke="var(--royal-blue)" d="M363 420 V512 Q363 567 413 567 Q464 567 464 616 V863"/>
      <path stroke="var(--royal-blue)" d="M591 420 V512 Q591 567 541 567 Q490 567 490 616 V863"/>
      <path stroke="var(--path-red)" d="M252 610 Q258 683 337 683 Q437 683 437 765 V863"/>
      <path stroke="var(--path-red)" d="M700 610 Q694 683 602 683 Q517 683 517 765 V863"/>
    </g>

    <!-- compass -->
    <g class="compass" role="img" aria-label="Compass rose marking the shared values at the centre">
      <ellipse cx="478" cy="1009" rx="132" ry="88" fill="url(#compass-fill)"/>
      <ellipse cx="478" cy="1009" rx="130" ry="86" fill="none" stroke="var(--brand-red)" stroke-width="3"/>
      <ellipse cx="478" cy="1009" rx="124" ry="81" fill="none" stroke="var(--royal-blue)" stroke-width="1.5"/>
    </g>

    <!-- pen nib -->
    <polygon points="430,866 525,866 478,1006" fill="#cfcfcf"/>
    <polygon points="454,866 501,866 478,1006" fill="#6b6b6b"/>

    <!-- value words circling the compass -->
    <text class="value-word"><textPath href="#value-ring" startOffset="58.6%" text-anchor="middle">Values</textPath></text>
    <text class="value-word"><textPath href="#value-ring" startOffset="90.6%" text-anchor="middle">Morals</textPath></text>
    <text class="value-word"><textPath href="#value-ring" startOffset="9.5%" text-anchor="middle">Principles</textPath></text>
    <text class="value-word"><textPath href="#value-ring" startOffset="39.5%" text-anchor="middle">Ethics</textPath></text>

    <!-- Aspiration -->
    <g class="disc disc--aspiration" filter="url(#disc-shadow)">
      <circle cx="363" cy="349" r="82" fill="url(#red-rim)"/>
      <circle cx="363" cy="349" r="74" fill="url(#red-disc)"/>
    </g>
    <g class="icon-target" fill="none" stroke="#fff">
      <circle cx="360" cy="350" r="46" stroke-width="10"/>
      <circle cx="360" cy="350" r="27" stroke-width="9"/>
      <circle cx="360" cy="350" r="9" stroke-width="5"/>
      <line x1="360" y1="350" x2="398" y2="312" stroke-width="6"/>
      <polygon points="392,302 404,298 400,312 412,318 398,322" fill="#fff" stroke="none"/>
    </g>

    <!-- Agility -->
    <g class="disc disc--agility" filter="url(#disc-shadow)">
      <circle cx="590" cy="349" r="82" fill="url(#red-rim)"/>
      <circle cx="590" cy="349" r="74" fill="url(#red-disc)"/>
    </g>
    <g class="icon-speed" stroke="#fff" stroke-linecap="round" fill="none">
      <line x1="530" y1="353" x2="572" y2="350" stroke-width="6"/>
      <line x1="528" y1="364" x2="566" y2="362" stroke-width="6"/>
      <line x1="534" y1="375" x2="562" y2="374" stroke-width="6"/>
      <polyline points="588,318 624,350 588,382" stroke-width="12" stroke-linejoin="round"/>
    </g>

    <!-- Agency -->
    <g class="disc disc--agency" filter="url(#disc-shadow)">
      <circle cx="252" cy="536" r="82" fill="url(#blue-rim)"/>
      <circle cx="252" cy="536" r="74" fill="url(#blue-disc)"/>
    </g>
    <g class="icon-expand" fill="none" stroke="#fff">
      <circle cx="252" cy="536" r="44" stroke-width="9"/>
      <circle cx="252" cy="536" r="26" stroke-width="8"/>
      <g stroke-width="5" stroke-linecap="round">
        <line x1="218" y1="502" x2="208" y2="492"/>
        <line x1="286" y1="502" x2="296" y2="492"/>
        <line x1="218" y1="570" x2="208" y2="580"/>
        <line x1="286" y1="570" x2="296" y2="580"/>
      </g>
      <g fill="#fff" stroke="none">
        <polygon points="205,489 219,490 206,503"/>
        <polygon points="299,489 285,490 298,503"/>
        <polygon points="205,583 219,582 206,569"/>
        <polygon points="299,583 285,582 298,569"/>
      </g>
    </g>

    <!-- Altitude -->
    <g class="disc disc--altitude" filter="url(#disc-shadow)">
      <circle cx="700" cy="536" r="82" fill="url(#blue-rim)"/>
      <circle cx="700" cy="536" r="74" fill="url(#blue-disc)"/>
    </g>
    <g class="icon-summit" fill="#fff">
      <polygon points="677,579 716,522 747,579"/>
      <polygon points="659,579 680,546 688,552 670,579"/>
      <rect x="710" y="494" width="4" height="30"/>
      <polygon points="714,495 736,497 730,504 736,511 714,510"/>
      <path d="M690 561 Q705 550 718 558 Q728 564 740 560" fill="none" stroke="#3639bb" stroke-width="4"/>
    </g>
  </svg>

  <section class="trait trait--left trait--top">
    <p class="trait-label">Learners with <strong>Aspiration</strong></p>
    <p>Inspired and Believe in persuing great things</p>
  </section>
  <section class="trait trait--right trait--top trait--agility">
    <p class="trait-label">Learners with <strong>Agility</strong></p>
    <p>Are determined, equipped and able to accomplish great things</p>
  </section>
  <section class="trait trait--left trait--bottom trait--agency">
    <p class="trait-label">Learners with <strong>Agency</strong></p>
    <p>Believe in their capacity and responsibility to do great things</p>
  </section>
  <section class="trait trait--right trait--bottom">
    <p class="trait-label">Learners with <strong>Altitude</strong></p>
    <p>Achieve great things and work to elevate others</p>
  </section>

  <div class="footer-band"></div>
</main>
</body>
</html>
```